New template needed for Joomla 3.2 website

We are a mortgage origination company based in Johannesburg, South Africa and require a sleek, modern & professional look for our website.
The website is complete and your template should accommodate all pages on the site (there are not many) and be ready for Joomla implementation.
Our website can be viewed at www.keystonelending.example.co.za
Target Market(s)
We are targeting consumers who require mortgage finance to buy real estate. There is no particular demographic, except that we cater to South African home buyers exclusively!
Requirements
Must have
- It must look professional and modern.
Take a look at competitor websites:
www.vundo.example.co.za
www.zqbondhub.example.com
http://www.brightpathfold.example.co.za/loanpeak/
http://www.tideloan.example.co.za/
We want to beat the competition !!
Nice to have
- Website should blend with company logo and play on the symbol in the logo.
I want more of a people / photo element to the template. It needs to make us seem "tangible"

```html
<!DOCTYPE html>
<html lang="en">
<head>
<meta charset="utf-8">
<title>Keystone Lending – Property Finance Made Easy</title>
<link rel="stylesheet" href="https://fonts.googleapis.com/css2?family=Lato:wght@400;700;900&display=swap">
<style>
  :root{
    --blue:#0a78b4;
    --blue-dark:#0b5f8f;
    --top-bar:#3c86c7;
    --navy:#124e75;
    --ink:#1f2326;
    --grey-text:#55595c;
    --page-bg:#e8e6e1;
    --panel:#ffffff;
    --line:#cfd2d4;
    --lower-bg:#eeeff2;
  }
  *{box-sizing:border-box;margin:0;padding:0}
  html,body{width:831px;height:1200px;overflow:hidden}
  body{font-family:"Lato",sans-serif;color:var(--ink);background:var(--page-bg);position:relative}

  .top-bar{position:absolute;left:0;top:0;width:831px;height:35px;background:var(--top-bar);border-bottom:2px solid #2f6fa8}
  .social{position:absolute;right:60px;top:8px;display:flex;gap:5px}
  .social span{width:18px;height:18px;border-radius:3px;background:#1d5d96;border:1px solid #cfe1f1}

  .site-header{position:absolute;left:0;top:35px;width:831px;height:145px;background:#fff}
  .brand{position:absolute;left:62px;top:32px;display:flex;align-items:center;gap:8px}
  .brand-dot{width:52px;height:52px;border-radius:50%;background:var(--blue)}
  .brand-name{font-weight:900;font-size:31px;color:var(--blue);letter-spacing:.5px;line-height:1}
  .brand-tag{position:absolute;left:120px;top:76px;font-weight:700;font-size:13px;color:var(--ink);letter-spacing:.3px}
  .call{position:absolute;right:65px;top:30px;font-weight:900;font-size:20px;color:var(--blue-dark)}
  .banks-title{position:absolute;right:65px;top:65px;font-weight:900;font-size:12px}
  .banks{position:absolute;right:65px;top:81px;font-weight:700;font-size:8px;color:var(--grey-text)}
  .main-nav{position:absolute;left:0;width:831px;top:118px;display:flex;justify-content:center;gap:15px;font-weight:700;font-size:12.5px;color:var(--navy)}
  .main-nav a{color:inherit;text-decoration:none}
  .swoosh{position:absolute;left:0;display:block}

  .slider{position:absolute;left:81px;top:231px;width:667px;height:343px;background:#fff;border-radius:4px;box-shadow:0 1px 5px rgba(0,0,0,.3);padding:5px}
  .slide-photo{width:100%;height:100%;background:linear-gradient(180deg,#3a3a3a 0%,#9a9a9a 35%,#6b6b6b 60%,#262626 100%)}
  .caption{position:absolute;left:236px;top:58px;width:426px;height:115px;background:rgba(40,40,40,.72);color:#fff;text-align:right;padding:12px 18px 0 0}
  .caption h1{font-weight:700;font-size:24px;line-height:30px;text-shadow:0 1px 2px #000}
  .caption p{font-weight:700;font-size:16px;margin-top:5px}
  .dots{position:absolute;left:382px;top:322px;display:flex;gap:4px}
  .dots span{width:9px;height:9px;border-radius:50%;background:#111}
  .dots span:first-child{background:#ddd}

  .features{position:absolute;left:83px;top:605px;width:668px;height:172px;background:var(--panel);border-radius:6px;box-shadow:0 1px 5px rgba(0,0,0,.3)}
  .feature{position:absolute;top:38px;width:196px;height:114px;border:1px solid var(--line);padding:20px 8px 0 14px;font-size:9.4px;line-height:11.9px;color:var(--ink)}
  .feature h2{position:absolute;left:22px;top:-14px;width:156px;height:25px;background:var(--blue);color:#fff;border-radius:3px;font-weight:400;font-size:14px;line-height:25px;text-align:center}
  .f1{left:20px}.f2{left:236px}.f3{left:450px}

  .lower{position:absolute;left:0;top:835px;width:831px;height:277px;background:linear-gradient(90deg,#dfe0e4,#f6f6f8 50%,#dfe0e4)}
  .divider-v{position:absolute;left:423px;top:20px;width:1px;height:240px;background:var(--line)}
  .divider-h{position:absolute;left:113px;top:131px;width:628px;height:1px;background:var(--line)}
  .cta{position:absolute;width:300px}
  .cta h3{font-weight:700;font-size:15px;color:var(--blue)}
  .cta p{font-size:14px;line-height:18px;margin-top:17px;color:var(--ink)}
  .cta .btn{display:inline-block;margin-top:6px;background:var(--blue);color:#fff;font-size:14px;padding:4px 10px;border-radius:3px}
  .left{right:426px;text-align:right}
  .right{left:441px}

  .site-footer{position:absolute;left:0;top:1112px;width:831px;height:88px;background:linear-gradient(180deg,#3a9fd6,#0a6fae);text-align:center}
  .footer-nav{margin-top:31px;display:flex;justify-content:center;gap:16px;font-size:12px;color:#0c2c44}
  .fine{font-size:9px;color:#0c2c44;margin-top:9px;line-height:11px}
</style>
</head>
<body>
  <div class="top-bar">
    <div class="social"><span></span><span></span><span></span><span></span></div>
  </div>

  <header class="site-header">
    <div class="brand"><div class="brand-dot"></div><div class="brand-name">KEYSTONE LENDING</div></div>
    <div class="brand-tag">PROPERTY FINANCE MADE EASY</div>
    <div class="call">CALL: (010) 555 0142</div>
    <div class="banks-title">WE RAISE YOUR HOMELOAN WITH:</div>
    <div class="banks">ACREBANK . NORTHVALE . CAPEFIN . STONEBANK . SA BONDWORKS . RIVERMARK . IVORYCAP</div>
    <nav class="main-nav">
      <a>Home</a><a>About Keystone</a><a>Important Information</a><a>Homeloan Calculators</a><a>Apply On-Line</a><a>Contact Keystone</a>
    </nav>
  </header>
  <svg class="swoosh" style="top:176px" width="831" height="14" viewBox="0 0 831 14">
    <path d="M0 2 Q415 14 831 2 L831 14 L0 14Z" fill="var(--blue)"/>
    <path d="M0 0 Q415 12 831 0 L831 2 Q415 14 0 2Z" fill="#fff"/>
  </svg>

  <section class="slider">
    <div class="slide-photo" role="img" aria-label="Black and white photo of people silhouetted at a glass wall overlooking a city skyline"></div>
    <div class="caption">
      <h1>Welcome to Keystone Lending<br>Property Finance Made Easy</h1>
      <p>FAST HOMELOANS . GREAT SERVICE !</p>
    </div>
    <div class="dots"><span></span><span></span><span></span><span></span></div>
  </section>

  <section class="features">
    <div class="feature f1"><h2>100% Free of Charge</h2>No hidden costs or service charges. Our fee is not hidden within the finance charges of your homeloan. We guarantee a 100% free of charge, first class service to you. Our fees are paid by the banks, regardless of your home-loan.</div>
    <div class="feature f2"><h2>Exceptional Service</h2>No hidden costs or service charges. Our fee is not hidden within the finance charges of your homeloan. We guarantee a 100% free of charge, first class service to you. Our fees are paid by the banks, regardless of your home-loan.</div>
    <div class="feature f3"><h2>Credit Help</h2>No hidden costs or service charges. Our fee is not hidden within the finance charges of your homeloan. We guarantee a 100% free of charge, first class service to you. Our fees are paid by the banks, regardless of your home-loan.</div>
  </section>

  <svg class="swoosh" style="top:822px" width="831" height="14" viewBox="0 0 831 14">
    <path d="M0 14 Q415 -4 831 14 L831 12 Q415 -8 0 12Z" fill="var(--blue-dark)"/>
    <path d="M0 12 Q415 -8 831 12 L831 0 L0 0Z" fill="var(--page-bg)"/>
    <path d="M0 12 Q415 -2 831 12 L831 14 L0 14Z" fill="var(--blue)"/>
  </svg>

  <section class="lower">
    <div class="divider-v"></div>
    <div class="divider-h"></div>
    <div class="cta left" style="top:20px"><h3>Referral Program</h3><p>Click on the button below to join our lead referal program and start earning money.</p><span class="btn">Join Today</span></div>
    <div class="cta right" style="top:20px"><h3>Get Pre Qualified</h3><p>Our experienced consultants would be happy to prequalify you for a homeloan.</p><span class="btn">Apply Now</span></div>
    <div class="cta left" style="top:160px"><h3>Ask a Question</h3><p>Ask an experienced consultant to answer all your questions about homeloan finance.</p><span class="btn">Ask Now</span></div>
    <div class="cta right" style="top:160px"><h3>Calculators</h3><p>Find out what you can afford with our convenient finance calculators.</p><span class="btn">Calculate</span></div>
  </section>

  <svg class="swoosh" style="top:1104px" width="831" height="14" viewBox="0 0 831 14">
    <path d="M0 8 Q415 -2 831 8 L831 14 L0 14Z" fill="#3a9fd6"/>
    <path d="M0 8 Q415 -2 831 8 L831 0 L0 0Z" fill="#e4e5e9"/>
    <path d="M0 8 Q415 -2 831 8 L831 10 Q415 0 0 10Z" fill="var(--blue-dark)"/>
  </svg>
  <footer class="site-footer">
    <nav class="footer-nav"><span>Privacy</span><span>Policy</span><span>About Keystone</span><span>Contact Keystone</span></nav>
    <p class="fine">Built with HTML5 and CSS3<br>Copyright © 2014 Keystone Lending (Pty) Ltd</p>
  </footer>
</body>
</html>
```